Scandinavian film company needs new website

We need a new web design for our company based in Roskilde, Denmark called Talvek Film (translated: Elk Film).

We are a creative company that make video content to social media and provides professional photographers and technicians for multi-camera productions.

We want a scroll-down site where everything is accessible on the same page. The individual elements of the page must be accessible by a menu bar at the top.

The design should be a wordpress template or the like, which we can edit and work with on our own after delivery.

The color scheme must be consistent with one of the attached logo designs - but are welcome to come up with complementary colors to match the logo colors. We prefer black/dark grey background over white.

We've attached some atmospheric photos from our workplaces and some equipment photos which can be used or be inspiration for background design.

Websites for inspiration:
http://vomatu.example/
- inspired by color scheme and the simple structure of the website.

http://www.parnowickholster.example/
- inspired by background photos that does not move and simple structure of the website.

http://fomkar.example/
- inspired by the simple structure of the website

http://www.plumvaneworks.example/
- inspired by the simple structure of the frontpage

The website should contain:

Profile
- Hvem er vi (english: Who we are)
- Hvorfor vælge os (english: why pick us)
- Sådan kommer du godt i gang (english: how do you get started)

Services
- Videoproduktion
- Animationsfilm
- Redigering (english: editing)
- OB-produktion

Portfolio (video gallery)

References (minimum 8 logos)

Follow us (Vimeo / Youtube / Pinterest / Instagram)

Contact

Target Market(s)

Communication and marketing departments in large and medium-sized Danish companies

Industry/Entity Type

Videography

Coding

Coded - Design and coding required

Number of Pages Required

1 page

Font styles to use
Sans Serif

Colors
000000
333333
3276b5
fbf289

Requirements
Must have
• - Logo
• - Responsive design (videos must look good on mobile devices)
• - Color scheme must be consistent with one of the attached logo designs - we prefer black/dark grey backgrounds.
• - The code/design should be a wordpress template or the like, which we can edit and work with on our own after delivery.
• Website should contain:
• Talvek Film
• - Hvem er vi (english: Who we are)
• - Hvorfor vælge os (english: why pick us)
• - Sådan kommer du godt i gang (english: how do you get started)
• Services
• - Videoproduktion
• - Animationsfilm
• - Redigering (english: editing)
• - OB-produktion
• Portfolio (video gallery)
• References (minimum 8 logos)
• Follow us (Vimeo / Youtube / Pinterest / Instagram)
• Contact
Should not have
• Contact formular
• Subpages
• Unnecessary elements

```html
<!DOCTYPE html>
<html lang="da">
<head>
<meta charset="utf-8">
<title>Talvek Film – Videoproduktion</title>
<link rel="stylesheet" href="https://fonts.googleapis.com/css2?family=Oswald:wght@300;400;500&family=Open+Sans:wght@400;600&display=swap">
<style>
:root{
  --yellow:#e6d24f;
  --yellow-soft:#fbf289;
  --teal:#0f3b3f;
  --teal-deep:#0b2f33;
  --dark:#151616;
  --dark-2:#1d1e1e;
  --white:#ffffff;
  --muted:#c9cccb;
  --grey:#8a8d8c;
}
*{box-sizing:border-box;margin:0;padding:0}
html,body{width:1200px;height:4639px;overflow:hidden}
body{background:var(--dark);color:var(--white);font-family:"Open Sans",Arial,sans-serif;position:relative}
section,header,footer{position:absolute;left:0;width:1200px}
.abs{position:absolute}
.heading{font-family:"Oswald",Arial,sans-serif;font-weight:400;text-transform:uppercase;text-align:center;width:1200px;left:0}
.heading .accent{color:var(--yellow)}
.divider{position:absolute;left:500px;width:200px;height:20px}

/* header */
.site-header{top:0;height:773px;background:radial-gradient(ellipse at 72% 45%,#5a5d5c 0%,#2e3030 40%,#121313 85%)}
.nav-bar{position:absolute;top:0;left:0;width:1200px;height:108px;background:rgba(10,12,12,.55)}
.brand-box{position:absolute;left:80px;top:18px;width:72px;height:72px;border:2px solid var(--yellow);display:flex;align-items:center;justify-content:center;font-size:12px;color:var(--yellow);text-align:center;line-height:1.2}
.menu{position:absolute;top:38px;right:78px;display:flex;gap:38px;list-style:none;font-size:13px}
.menu li{padding:6px 12px;color:var(--white)}
.menu li.active{border:1px solid var(--yellow);color:var(--yellow)}
.hero-logo{position:absolute;left:510px;top:258px;width:180px;height:180px;border:3px solid var(--yellow);display:flex;flex-direction:column;align-items:center;justify-content:center;gap:14px;color:var(--yellow);font-size:26px}
.hero-logo .dot{width:70px;height:70px;border-radius:50%;background:var(--yellow)}
.hero-title{top:480px;font-size:60px;letter-spacing:1px}
.hero-text{position:absolute;left:300px;top:572px;width:600px;font-size:14px;line-height:1.75;text-align:center;color:var(--muted)}
.hero-reel{position:absolute;left:582px;top:724px;width:36px;height:36px;border-radius:50%;background:var(--yellow-soft)}

/* profile */
.profile{top:773px;height:749px;background:var(--teal)}
.profile .heading{top:72px;font-size:36px}
.profile .divider{top:130px}
.profile-col{position:absolute;top:220px;width:300px;text-align:center}
.profile-col h3{font-family:"Oswald",sans-serif;font-weight:400;color:var(--yellow);font-size:22px}
.icon-box{width:142px;height:142px;border:2px solid var(--yellow);margin:30px auto 0;display:flex;align-items:center;justify-content:center}
.profile-col p{margin-top:34px;font-size:13px;line-height:1.75;color:var(--muted);text-align:justify}
.read-more{position:absolute;top:634px;width:360px;height:52px}
.read-more::before,.read-more::after{content:"";position:absolute;top:26px;width:130px;height:1px;background:var(--yellow)}
.read-more::before{left:0}.read-more::after{right:0}
.read-more span{position:absolute;left:150px;top:0;width:60px;height:52px;border:1px solid var(--yellow);font-family:"Oswald",sans-serif;font-size:12px;line-height:1.3;display:flex;align-items:center;justify-content:center;text-align:center}

/* services */
.services{top:1522px;height:659px;background:radial-gradient(ellipse at 50% 55%,#2a2b2b 0%,#151616 75%)}
.services .heading{top:66px;font-size:32px}
.services .divider{top:124px}
.services .lead{position:absolute;left:240px;top:170px;width:720px;font-size:13px;line-height:1.7;text-align:center;color:var(--muted)}
.service{position:absolute;top:270px;width:260px;text-align:center}
.service .ring{width:146px;height:146px;margin:0 auto;border-radius:50%;background:var(--yellow);border:6px solid #4a4a3a;display:flex;align-items:center;justify-content:center}
.service h4{margin-top:40px;font-family:"Oswald",sans-serif;font-weight:500;font-size:18px;color:var(--yellow);text-transform:uppercase}
.service p{margin-top:12px;font-size:13px;line-height:1.65;color:var(--muted)}

/* gallery */
.gallery{top:2181px;height:989px;background:var(--teal)}
.gallery .heading{top:58px;font-size:34px}
.gallery .divider{top:114px}
.tile{position:absolute;overflow:hidden}
.tile .play{position:absolute;border-radius:50%;border:3px solid var(--yellow);display:flex;align-items:center;justify-content:center}
.tile .caption{position:absolute;left:0;width:100%;text-align:center;font-family:"Oswald",sans-serif;text-transform:uppercase;color:var(--white)}
.view-all{position:absolute;left:572px;top:887px;width:56px;height:62px;border:1px solid var(--white);font-family:"Oswald",sans-serif;font-size:15px;line-height:1.25;display:flex;align-items:center;justify-content:center;text-align:center}

/* references */
.references{top:3170px;height:619px;background:var(--dark)}
.references .heading{top:64px;font-size:34px}
.references .divider{top:122px}
.references .lead{position:absolute;left:0;width:1200px;top:152px;text-align:center;font-size:13px;color:var(--grey)}
.ref-logo{position:absolute;width:110px;height:110px;display:flex;align-items:center;justify-content:center}

/* contact */
.contact{top:3789px;height:411px;background:linear-gradient(180deg,#0c3135 0%,#123f43 100%)}
.contact .heading{top:60px;font-size:32px}
.contact .divider{top:124px}
.contact-name{position:absolute;left:0;width:1200px;top:190px;text-align:center;font-family:"Oswald",sans-serif;font-weight:400;font-size:24px;color:var(--yellow)}
.contact-name .sep,.contact-name .person{color:var(--white)}
.contact-item{position:absolute;top:276px;display:flex;align-items:center;gap:22px;font-family:"Oswald",sans-serif;font-size:25px;color:var(--yellow);white-space:nowrap}
.square-icon{width:46px;height:46px;border:2px solid var(--white);display:flex;align-items:center;justify-content:center;flex:none}
.social{position:absolute;top:276px;width:46px;height:46px;border:2px solid var(--white)}

/* map */
.map{top:4200px;height:371px;background:linear-gradient(160deg,#dfe3d6 0%,#cfd8c0 45%,#e7e6d8 100%)}
.map-box{position:absolute;left:541px;top:93px;width:337px;height:139px;background:var(--teal);text-align:center;padding-top:30px}
.map-box h5{font-family:"Oswald",sans-serif;font-weight:400;font-size:20px;color:var(--yellow)}
.map-box p{margin-top:6px;font-size:13px;line-height:1.6;color:var(--muted)}

/* footer */
.site-footer{top:4571px;height:68px;background:var(--yellow)}
.footer-brand{position:absolute;left:60px;top:10px;display:flex;align-items:center;gap:16px;font-weight:600;font-size:24px;color:var(--dark)}
.footer-brand .mark{width:48px;height:48px;border-radius:50%;background:var(--dark)}
.footer-legal{position:absolute;right:90px;top:24px;font-size:12px;color:#333;display:flex;gap:18px}
.footer-legal b{font-weight:600}
</style>
</head>
<body>

<header class="site-header" id="welcome">
  <div class="abs" role="img" aria-label="Concert stage with lighting rig, dark photo backdrop" style="inset:0;background:radial-gradient(ellipse at 78% 40%,rgba(140,140,130,.35) 0%,rgba(0,0,0,0) 55%)"></div>
  <div class="nav-bar">
    <div class="brand-box">Talvek<br>Film</div>
    <ul class="menu">
      <li class="active">Welcome</li>
      <li>Profile</li>
      <li>Services</li>
      <li>Portfolio</li>
      <li>References</li>
      <li>Contact</li>
    </ul>
  </div>
  <div class="hero-logo"><span class="dot"></span>Talvek Film</div>
  <h1 class="heading abs hero-title">Videoproduktion</h1>
  <p class="hero-text">Talvek Film leverer videoproduktioner og videofotografer til små og store danske virksomheder og organisationer. Vi tager hånd om alle faser i en videoproduktion – fra idé til færdig film, så det eneste du skal gøre, er at være åben du få produceret reklamefilm, animationsfilm, præsentationsfilm ønsker og behov.</p>
  <div class="hero-reel"></div>
</header>

<section class="profile" id="profile">
  <h2 class="heading abs">Our <span class="accent">Profile</span></h2>
  <svg class="divider" viewBox="0 0 200 20"><line x1="40" y1="10" x2="88" y2="10" stroke="#e6d24f"/><line x1="112" y1="10" x2="160" y2="10" stroke="#e6d24f"/><circle cx="100" cy="10" r="6" fill="none" stroke="#e6d24f" stroke-width="2"/></svg>

  <div class="profile-col" style="left:110px">
    <h3>Hvem er vi?</h3>
    <div class="icon-box"><svg width="60" height="50" viewBox="0 0 60 50" fill="#e6d24f"><circle cx="30" cy="14" r="9"/><path d="M14 46c0-10 7-17 16-17s16 7 16 17z"/><circle cx="12" cy="18" r="6"/><circle cx="48" cy="18" r="6"/><path d="M0 42c0-7 5-12 12-12 2 0 4 .5 5 1-3 3-5 7-5 11z"/><path d="M60 42c0-7-5-12-12-12-2 0-4 .5-5 1 3 3 5 7 5 11z"/></svg></div>
    <p>Talvek Film leverer videoproduktioner og videofotografer til små og store danske virksomheder og organisationer. Vi tager hånd om alle faser i en videoproduktion fra idé til færdig film, så det eneste du skal gøre, er at være åben omkring dine ønsker og behov.</p>
  </div>
  <div class="profile-col" style="left:450px">
    <h3>Hvorfor vælge os?</h3>
    <div class="icon-box"><svg width="52" height="52" viewBox="0 0 52 52" fill="#e6d24f"><rect x="2" y="22" width="10" height="26"/><path d="M16 22l10-18c4 0 6 3 5 7l-2 9h16c4 0 6 3 5 6l-5 18c-1 3-3 4-6 4H16z"/></svg></div>
    <p>Din vision er vores mission. Vi er ikke stødt på en opgave vi ikke kunne klare. Når du som klient bliver sat op til et uforpligtende introduktionsmøde med os, bliver du vejledt bedst muligt gennem projektet. Vi er stolte over at vi altid leverer video til stive virksomheder.</p>
  </div>
  <div class="profile-col" style="left:808px">
    <h3>Hvordan kommer du godt i gang?</h3>
    <div class="icon-box"><svg width="56" height="40" viewBox="0 0 56 40" fill="#e6d24f"><rect x="0" y="4" width="38" height="32" rx="4"/><path d="M40 16l16-10v28L40 24z"/></svg></div>
    <p>Vores erfaring viser, at jo tidligere vi bliver inkluderet i dine overvejelser om at lave en film jo bedre bliver for løbet og resultatet. Få uforpligtende sparring på dine idéer så du undgår faldgruber og udnytter det potentiale der er i at vælge den rigtige løsning fra starten.</p>
  </div>

  <div class="read-more" style="left:80px"><span>READ<br>MORE</span></div>
  <div class="read-more" style="left:420px"><span>READ<br>MORE</span></div>
  <div class="read-more" style="left:778px"><span>READ<br>MORE</span></div>
</section>

<section class="services" id="services">
  <h2 class="heading abs">Kompetencer</h2>
  <svg class="divider" viewBox="0 0 200 20"><circle cx="100" cy="10" r="6" fill="none" stroke="#e6d24f" stroke-width="2"/></svg>
  <p class="lead">It is a long established fact that a reader will be distracted by the readable content of a page when looking at its layout. The normal distribution of letters, as opposed to using making it look like readable English.</p>

  <div class="service" style="left:74px">
    <div class="ring"><svg width="50" height="50" viewBox="0 0 52 52" fill="#fff"><rect x="2" y="22" width="10" height="26"/><path d="M16 22l10-18c4 0 6 3 5 7l-2 9h16c4 0 6 3 5 6l-5 18c-1 3-3 4-6 4H16z"/></svg></div>
    <h4>Videoproduktion</h4>
    <p>It is a long established fact that a reader will be distracted by the readbook like readable English.</p>
  </div>
  <div class="service" style="left:328px">
    <div class="ring"><svg width="52" height="44" viewBox="0 0 52 44" fill="none" stroke="#fff" stroke-width="4"><rect x="2" y="2" width="48" height="40"/><path d="M6 38l14-16 10 10 6-6 12 12" fill="#fff" stroke="none"/><circle cx="36" cy="14" r="4" fill="#fff" stroke="none"/></svg></div>
    <h4>Videofotograf</h4>
    <p>It is a long established fact that a reader will be distracted by the readbook like readable English.</p>
  </div>
  <div class="service" style="left:600px">
    <div class="ring"><svg width="56" height="40" viewBox="0 0 56 40" fill="none" stroke="#fff" stroke-width="4"><rect x="8" y="2" width="40" height="28"/><line x1="0" y1="37" x2="56" y2="37"/></svg></div>
    <h4>Flerkameraproduktion</h4>
    <p>It is a long established fact that a reader will be distracted by the readbook like readable English.</p>
  </div>
  <div class="service" style="left:875px">
    <div class="ring"><svg width="54" height="44" viewBox="0 0 54 44" fill="none" stroke="#fff" stroke-width="4"><rect x="2" y="8" width="50" height="34" rx="3"/><rect x="18" y="2" width="18" height="6"/><circle cx="27" cy="25" r="9"/></svg></div>
    <h4>Tekniker</h4>
    <p>It is a long established fact that a reader will be distracted by the readbook like readable English.</p>
  </div>
</section>

<section class="gallery" id="portfolio">
  <h2 class="heading abs">Video Gallery</h2>
  <svg class="divider" viewBox="0 0 200 20"><line x1="40" y1="10" x2="88" y2="10" stroke="#e6d24f"/><line x1="112" y1="10" x2="160" y2="10" stroke="#e6d24f"/><circle cx="100" cy="10" r="6" fill="none" stroke="#e6d24f" stroke-width="2"/></svg>

  <div class="tile" role="img" aria-label="Video still: group of friends outdoors on a sunny day" style="left:83px;top:185px;width:653px;height:464px;background:linear-gradient(135deg,#8fb0c8 0%,#a89a80 50%,#5d5448 100%)">
    <div class="play" style="left:296px;top:200px;width:64px;height:64px"><svg width="22" height="24"><path d="M2 2l18 10L2 22z" fill="#e6d24f"/></svg></div>
    <div class="caption" style="top:388px;font-size:44px">Weekend Hobbies</div>
  </div>
  <div class="tile" role="img" aria-label="Video still: portrait in warm sunlight" style="left:764px;top:185px;width:350px;height:217px;background:linear-gradient(135deg,#c9b79c 0%,#7e6a55 100%)">
    <div class="play" style="left:150px;top:82px;width:50px;height:50px"><svg width="18" height="20"><path d="M2 2l14 8L2 18z" fill="#e6d24f"/></svg></div>
    <div class="caption" style="top:170px;font-size:17px">Summer Fashion</div>
  </div>
  <div class="tile" role="img" aria-label="Video still: mountain landscape at sunrise" style="left:764px;top:426px;width:350px;height:217px;background:linear-gradient(180deg,#6f8fa8 0%,#c99a60 55%,#3a3a3e 100%)">
    <div class="play" style="left:150px;top:72px;width:50px;height:50px"><svg width="18" height="20"><path d="M2 2l14 8L2 18z" fill="#e6d24f"/></svg></div>
    <div class="caption" style="top:170px;font-size:17px">Good Morning Ida</div>
  </div>

  <div class="tile" role="img" aria-label="Video still: cycling at sunset" style="left:83px;top:677px;width:239px;height:161px;background:linear-gradient(135deg,#d49a55,#6b4a30)"><div class="play" style="left:98px;top:58px;width:44px;height:44px"><svg width="16" height="18"><path d="M2 2l12 7L2 16z" fill="#e6d24f"/></svg></div></div>
  <div class="tile" role="img" aria-label="Video still: picnic on a beach" style="left:346px;top:677px;width:242px;height:161px;background:linear-gradient(135deg,#c8b59a,#8a7560)"><div class="play" style="left:99px;top:58px;width:44px;height:44px"><svg width="16" height="18"><path d="M2 2l12 7L2 16z" fill="#e6d24f"/></svg></div></div>
  <div class="tile" role="img" aria-label="Video still: dinner table with candles" style="left:609px;top:677px;width:242px;height:161px;background:linear-gradient(135deg,#b07a3c,#3d2a1c)"><div class="play" style="left:99px;top:58px;width:44px;height:44px"><svg width="16" height="18"><path d="M2 2l12 7L2 16z" fill="#e6d24f"/></svg></div></div>
  <div class="tile" role="img" aria-label="Video still: couple in a cafe" style="left:875px;top:677px;width:241px;height:161px;background:linear-gradient(135deg,#a38a72,#4e3e34)"><div class="play" style="left:98px;top:58px;width:44px;height:44px"><svg width="16" height="18"><path d="M2 2l12 7L2 16z" fill="#e6d24f"/></svg></div></div>

  <div class="view-all">VIEW<br>ALL</div>
</section>

<section class="references" id="references">
  <h2 class="heading abs">Referencer</h2>
  <svg class="divider" viewBox="0 0 200 20"><line x1="40" y1="10" x2="88" y2="10" stroke="#e6d24f"/><line x1="112" y1="10" x2="160" y2="10" stroke="#e6d24f"/><circle cx="100" cy="10" r="6" fill="none" stroke="#e6d24f" stroke-width="2"/></svg>
  <p class="lead">It is a long established fact that a reader will be distracted by the readable content of a page when looking at its layout.</p>

  <div class="ref-logo" style="left:121px;top:273px"><svg width="80" height="80"><rect x="10" y="10" width="60" height="60" fill="#b9a63e"/></svg></div>
  <div class="ref-logo" style="left:313px;top:273px"><svg width="80" height="80"><circle cx="40" cy="40" r="32" fill="#b9a63e"/></svg></div>
  <div class="ref-logo" style="left:551px;top:273px"><svg width="80" height="80"><circle cx="40" cy="40" r="32" fill="#b9a63e"/></svg></div>
  <div class="ref-logo" style="left:762px;top:273px"><svg width="80" height="80"><circle cx="40" cy="40" r="32" fill="#b9a63e"/></svg></div>
  <div class="ref-logo" style="left:981px;top:273px"><svg width="80" height="80"><rect x="10" y="10" width="60" height="60" fill="#b9a63e"/></svg></div>
  <div class="ref-logo" style="left:121px;top:425px"><svg width="80" height="80"><circle cx="40" cy="40" r="32" fill="#b9a63e"/></svg></div>
  <div class="ref-logo" style="left:313px;top:425px"><svg width="80" height="80"><rect x="10" y="10" width="60" height="60" fill="#b9a63e"/></svg></div>
  <div class="ref-logo" style="left:551px;top:425px"><svg width="80" height="80"><rect x="10" y="10" width="60" height="60" fill="#b9a63e"/></svg></div>
  <div class="ref-logo" style="left:762px;top:425px"><svg width="80" height="80"><circle cx="40" cy="40" r="32" fill="#b9a63e"/></svg></div>
  <div class="ref-logo" style="left:981px;top:425px"><svg width="80" height="80"><circle cx="40" cy="40" r="32" fill="#b9a63e"/></svg></div>
</section>

<section class="contact" id="contact">
  <h2 class="heading abs">Kontakt</h2>
  <svg class="divider" viewBox="0 0 200 20"><line x1="40" y1="10" x2="88" y2="10" stroke="#e6d24f"/><line x1="112" y1="10" x2="160" y2="10" stroke="#e6d24f"/><circle cx="100" cy="10" r="6" fill="none" stroke="#e6d24f" stroke-width="2"/></svg>
  <p class="contact-name">Talvek Film <span class="sep">|</span> <span class="person">Jonas Vell Sørup</span></p>

  <div class="contact-item" style="left:80px">
    <span class="square-icon"><svg width="20" height="20" viewBox="0 0 20 20" fill="#fff"><path d="M4 1l4 4-2 3c1 2 3 4 5 5l3-2 4 4-3 4C8 18 2 12 1 4z"/></svg></span>
    +45 3890 1276
  </div>
  <div class="contact-item" style="left:370px">
    <span class="square-icon"><svg width="22" height="16" viewBox="0 0 22 16" fill="#fff"><path d="M0 0h22v2L11 9 0 2z"/><path d="M0 4l11 7 11-7v12H0z"/></svg></span>
    kontakt@talvekfilm.example
  </div>
  <span class="social" style="left:787px" aria-label="Follow us"></span>
  <span class="social" style="left:886px" aria-label="Follow us"></span>
  <span class="social" style="left:985px" aria-label="Follow us"></span>
  <span class="social" style="left:1072px" aria-label="Follow us"></span>
</section>

<section class="map" role="img" aria-label="Street map of the local area with the studio location marked">
  <div class="map-box">
    <h5>Location</h5>
    <p>Skovkrogen 8, 9170 Ellbyvik,<br>Denmark</p>
  </div>
  <svg class="abs" style="left:698px;top:244px" width="26" height="36" viewBox="0 0 26 36"><path d="M13 0C6 0 0 6 0 13c0 9 13 23 13 23s13-14 13-23C26 6 20 0 13 0z" fill="#333"/><circle cx="13" cy="13" r="5" fill="#dfe3d6"/></svg>
</section>

<footer class="site-footer">
  <div class="footer-brand"><span class="mark"></span>Talvek Film</div>
  <div class="footer-legal"><span>© 2015 Copyrights. All Rights Reserved.</span><b>SiteMap</b><span>|</span><b>Privacy Policy</b></div>
</footer>

</body>
</html>
```